New business card for my lawn and landscape business

Dorrin Yard and Building is a full-service lawn care, landscaping, and light construction company serving Paragould and the Northeast Arkansas region. The business is owned and operated by Marcus Toller, with a reputation for hands-on, detail-oriented service, dependable crews, and quality results for both residential and commercial clients. A well regarded business with great reviews.
Owner Marcus Toller
Dorrinyardandbuilding.example

Target Market(s)

Commercial, Middle, and upper class in north east Arkansas

Industry/Entity Type

Lawn maintenance and landscape

Contact Information for Business Card

Dorrin Yard And Building Professional lawn care, landscaping, and property improvement in Northeast Arkansas. • lawn maintenance •lawn treatments and weed control • exterior projects • Custom landscape design & installation • Sod, trees, rock & drainage solutions • Residential & commercial services Reliable. Detailed. Done right.

Requirements
Must have
• Business name, service area, list of some of our services, clean design that represents
Nice to have
• Unique. Different design element than just grass because its already in n the logo. Picture of a warm season (south) lawn or landscape. Pictures of the type of work we do

```html
<!DOCTYPE html>
<html lang="en">
<head>
<meta charset="utf-8">
<title>Dorrin Yard And Building – Business Card</title>
<link href="https://fonts.googleapis.com/css2?family=Poppins:wght@400;500;600;700&display=swap" rel="stylesheet">
<style>
  :root {
    --leaf-green: #7ab342;
    --paper: #ffffff;
    --ink: #4a4a4a;
    --ink-soft: #5c5c5c;
    --silver: #b9b9bb;
    --rule: #cfcfcf;
    --stage: #2a2a2a;
  }
  * { box-sizing: border-box; margin: 0; padding: 0; }
  html, body { width: 1200px; height: 880px; overflow: hidden; }
  body {
    background: var(--stage);
    font-family: "Poppins", sans-serif;
    position: relative;
  }
  .card {
    position: absolute;
    width: 560px;
    height: 320px;
    border-radius: 20px;
    overflow: hidden;
    box-shadow: 0 10px 30px rgba(0,0,0,0.45);
  }

  /* Services side */
  .card--services {
    left: 70px; top: 80px;
    background: var(--leaf-green);
    color: var(--paper);
    text-align: center;
  }
  .brand {
    display: inline-flex;
    align-items: center;
    gap: 10px;
    font-weight: 600;
    font-size: 24px;
    letter-spacing: 0.5px;
  }
  .brand__dot {
    width: 16px; height: 16px; border-radius: 50%;
    flex: none;
  }
  .card--services .brand { margin-top: 48px; }
  .card--services .brand__dot { background: var(--paper); }
  .services__title {
    margin-top: 30px;
    font-weight: 700;
    font-size: 17px;
    letter-spacing: 0.5px;
  }
  .services__list {
    list-style: none;
    margin: 10px auto 0;
    width: 470px;
    font-size: 13px;
    line-height: 22px;
  }
  .services__list li { display: inline; white-space: nowrap; margin: 0 5px; }
  .leaf { display: inline-block; width: 12px; height: 9px; vertical-align: -1px; margin-right: 5px; }

  /* Contact side */
  .card--contact {
    left: 570px; top: 480px;
    background: var(--paper);
  }
  .swoosh { position: absolute; inset: 0; }
  .card--contact .brand {
    position: absolute;
    left: 30px; top: 108px;
    width: 200px;
    color: var(--leaf-green);
    font-size: 22px;
    line-height: 1.2;
    text-align: left;
  }
  .card--contact .brand__dot { background: var(--leaf-green); }
  .divider {
    position: absolute;
    left: 262px; top: 56px;
    width: 1px; height: 130px;
    background: var(--rule);
  }
  .contact {
    position: absolute;
    left: 290px; top: 52px;
    color: var(--ink-soft);
    font-size: 12px;
    line-height: 17px;
  }
  .contact__name { font-size: 22px; font-weight: 400; color: var(--ink); line-height: 26px; }
  .contact__role { font-size: 14px; color: var(--leaf-green); margin-bottom: 10px; }
  .contact__address { margin-bottom: 8px; }
  .contact__line { display: flex; align-items: center; gap: 7px; }
  .icon-badge {
    width: 15px; height: 15px; border-radius: 50%;
    background: var(--leaf-green);
    display: inline-flex; align-items: center; justify-content: center;
  }
  .website {
    position: absolute;
    right: 28px; bottom: 26px;
    color: var(--paper);
    font-size: 13px;
  }
</style>
</head>
<body>

  <section class="card card--services">
    <div class="brand"><span class="brand__dot"></span>Dorrin Yard And Building</div>
    <h2 class="services__title">SERVICES</h2>
    <ul class="services__list">
      <li><svg class="leaf" viewBox="0 0 12 9"><path d="M0 8 C2 1 7 0 12 1 C10 6 6 9 0 8 Z" fill="#fff"/></svg>Lawn maintenance</li>
      <li><svg class="leaf" viewBox="0 0 12 9"><path d="M0 8 C2 1 7 0 12 1 C10 6 6 9 0 8 Z" fill="#fff"/></svg>Lawn treatments and weed control</li>
      <li><svg class="leaf" viewBox="0 0 12 9"><path d="M0 8 C2 1 7 0 12 1 C10 6 6 9 0 8 Z" fill="#fff"/></svg>Exterior projects</li>
      <li><svg class="leaf" viewBox="0 0 12 9"><path d="M0 8 C2 1 7 0 12 1 C10 6 6 9 0 8 Z" fill="#fff"/></svg>Custom landscape design &amp; installation</li>
      <li><svg class="leaf" viewBox="0 0 12 9"><path d="M0 8 C2 1 7 0 12 1 C10 6 6 9 0 8 Z" fill="#fff"/></svg>Sod, trees, rock &amp; drainage solutions</li>
      <li><svg class="leaf" viewBox="0 0 12 9"><path d="M0 8 C2 1 7 0 12 1 C10 6 6 9 0 8 Z" fill="#fff"/></svg>Residential &amp; commercial services</li>
    </ul>
  </section>

  <section class="card card--contact">
    <svg class="swoosh" viewBox="0 0 560 320" preserveAspectRatio="none" aria-hidden="true">
      <path d="M0 262 C210 258 380 225 560 98 L560 320 L0 320 Z" fill="var(--leaf-green)"/>
      <path d="M0 256 C220 250 400 200 545 92 C420 190 230 246 0 262 Z" fill="var(--silver)"/>
    </svg>

    <div class="brand"><span class="brand__dot"></span><span>Dorrin Yard<br>And Building</span></div>
    <div class="divider"></div>

    <div class="contact">
      <p class="contact__name">Marcus Toller</p>
      <p class="contact__role">Founder/Director</p>
      <p class="contact__address">PO BOX 480 Halden Lane<br>4th Street Paragould</p>
      <p class="contact__line">
        <span class="icon-badge"><svg width="7" height="9" viewBox="0 0 7 9"><rect x="0.7" y="0.5" width="5.6" height="8" rx="1" fill="none" stroke="#fff"/></svg></span>
        (870) 555 0142
      </p>
      <p class="contact__line">
        <span class="icon-badge"><svg width="9" height="7" viewBox="0 0 9 7"><rect x="0.5" y="0.5" width="8" height="6" fill="#fff"/><path d="M0.5 0.5 L4.5 4 L8.5 0.5" fill="none" stroke="#7ab342" stroke-width="0.8"/></svg></span>
        info@dorrinmail.example
      </p>
    </div>

    <p class="website">www.dorrinyardandbuilding.example</p>
  </section>

</body>
</html>
```